Unique business card design

Boutique coastal hotel suites - in need of clever stand out business card I have uploaded the logo that I had created through quill forge I want something that is clever and stands out from everyone else - 418 Brantwell Avenue Kettlepoint Harbor 99571 phone or text 907 -581-6142 www.primemarrowbysuites.com

Target Market(s)

Men and woman

Industry/Entity Type

Boutique coastal hotel

Contact Information for Business Card

Marrowby Suites Kettlepoint Harbor marrowby_suites@mailnest.net

Requirements
Must have
• Classy - clever -bold 907-581-6142 call or text

```html
<!DOCTYPE html>
<html lang="en">
<head>
<meta charset="utf-8">
<title>Marrowby Suites – Business Card</title>
<link rel="stylesheet" href="https://fonts.googleapis.com/css2?family=Montserrat:wght@400;600;700&family=Arimo:wght@400&display=swap">
<style>
  :root {
    --backdrop: #1b1b1b;
    --charcoal: #2b2a26;
    --cream: #efebe4;
    --gold: #f2cf3a;
    --navy: #2d4a6b;
    --ink: #141414;
    --mist: #b9b6ae;
    --paper-text: #f3f1ec;
  }
  * { margin: 0; padding: 0; box-sizing: border-box; }
  html, body {
    width: 1200px; height: 900px; overflow: hidden;
    background: var(--backdrop);
  }
  .canvas { position: relative; width: 1200px; height: 900px; }

  .card {
    position: absolute; left: 260px; width: 680px; height: 388px;
    overflow: hidden; box-shadow: 0 10px 28px rgba(0,0,0,.55);
  }
  .card-front { top: 45px; background: var(--charcoal); }
  .card-back  { top: 467px; background: var(--cream); }

  /* Front */
  .front-band {
    position: absolute; left: 0; right: 0; top: 62px; height: 238px;
    background: var(--cream);
    border-top: 4px solid var(--gold); border-bottom: 4px solid var(--gold);
  }
  .brand {
    position: absolute; left: 0; right: 0;
    display: flex; align-items: center; justify-content: center; gap: 14px;
    font-family: "Montserrat", sans-serif; font-weight: 600;
    color: var(--navy); letter-spacing: .08em; text-transform: uppercase;
  }
  .brand-mark { width: 22px; height: 22px; background: var(--navy); }
  .card-front .brand { top: 88px; font-size: 40px; }
  .brand-rule {
    position: absolute; left: 170px; right: 170px; top: 152px;
    height: 3px; background: var(--ink);
  }

  /* Back */
  .back-shape { position: absolute; inset: 0; }
  .card-back .brand { top: 110px; font-size: 34px; }
  .holder {
    position: absolute; left: 60px; top: 238px;
    font-family: "Montserrat", sans-serif;
  }
  .holder-name { color: var(--gold); font-weight: 700; font-size: 30px; }
  .holder-role { color: var(--mist); font-size: 14px; margin-top: 2px; }
  .address {
    position: absolute; left: 60px; top: 312px;
    display: flex; gap: 12px; align-items: flex-start;
    font-family: "Arimo", sans-serif; font-style: normal; color: var(--paper-text);
    font-size: 17px; line-height: 1.45;
  }
  .address svg { margin-top: 10px; }
  .contacts {
    position: absolute; right: 36px; top: 236px;
    list-style: none; text-align: right;
    font-family: "Arimo", sans-serif; color: var(--paper-text);
    font-size: 16px; line-height: 1.7;
  }
  .contacts li { display: flex; justify-content: flex-end; align-items: center; gap: 10px; }
  .icon { width: 16px; height: 16px; flex: none; }
</style>
</head>
<body>
<main class="canvas">

  <section class="card card-front" aria-label="Card front">
    <div class="front-band">
      <div class="brand"><span class="brand-mark"></span>Marrowby Suites</div>
      <div class="brand-rule"></div>
    </div>
  </section>

  <section class="card card-back" aria-label="Card back">
    <svg class="back-shape" width="680" height="388" viewBox="0 0 680 388" aria-hidden="true">
      <polygon points="0,226 46,226 56,244 72,212 680,212 680,388 0,388" fill="var(--charcoal)"/>
      <polyline points="0,224 46,224 56,240 71,210 680,210" fill="none" stroke="var(--gold)" stroke-width="3.5"/>
    </svg>

    <div class="brand"><span class="brand-mark"></span>Marrowby Suites</div>

    <div class="holder">
      <div class="holder-name">Lena Harwick</div>
      <div class="holder-role">Director</div>
    </div>

    <address class="address">
      <svg class="icon" viewBox="0 0 16 16" aria-hidden="true">
        <path d="M8 1a5 5 0 0 0-5 5c0 3.5 5 9 5 9s5-5.5 5-9a5 5 0 0 0-5-5zm0 7a2 2 0 1 1 0-4 2 2 0 0 1 0 4z" fill="var(--gold)"/>
      </svg>
      <span>418 Brantwell Avenue<br>Kettlepoint Harbor 99571</span>
    </address>

    <ul class="contacts">
      <li>907 581 6142
        <svg class="icon" viewBox="0 0 16 16" aria-hidden="true"><path d="M4 1.5l2.3 3-1.4 1.6c.8 1.8 2.2 3.2 4 4l1.6-1.4 3 2.3-1.3 2.5C7.5 13.5 2.5 8.5 1.5 3z" fill="var(--gold)"/></svg>
      </li>
      <li>marrowby_suites@mailnest.net
        <svg class="icon" viewBox="0 0 16 16" aria-hidden="true"><rect x="1" y="3.5" width="14" height="9.5" fill="var(--gold)"/><polyline points="1,3.5 8,9 15,3.5" fill="none" stroke="var(--charcoal)" stroke-width="1.4"/></svg>
      </li>
      <li>www.primemarrowbysuites.com
        <svg class="icon" viewBox="0 0 16 16" aria-hidden="true"><circle cx="8" cy="8" r="7" fill="var(--gold)"/><ellipse cx="8" cy="8" rx="3" ry="7" fill="none" stroke="var(--charcoal)" stroke-width="1.2"/><line x1="1" y1="8" x2="15" y2="8" stroke="var(--charcoal)" stroke-width="1.2"/></svg>
      </li>
    </ul>
  </section>

</main>
</body>
</html>
```